Corvelle Strategies business card

I need a business card for my new strategic consulting LLC, Corvelle Strategies. We specialize in helping people who care about broadband technology and telecommunications policy, and we're based in Washington DC. I'm looking for a card that says smart, credible, future-facing and signals a high level of expertise. It's DC, so there's clearly a limit to how crazy we can go with this card, but I am looking for a design that reflects a company that is comfortable with technology, policy, and having a little bit fun. I'm uploading my logo below, and I'd like to have it be part of the card design in some fashion.
Target Market(s)
Telecommunications and technology policy professionals
Industry/Entity Type
Technology policy
Contact Information for Business Card
Name of business, my name (Glen Mosswater), email (glen@corvellestrategies-example.com) , phone number (202-555-0148)phone number

```html
<!DOCTYPE html>
<html lang="en">
<head>
<meta charset="utf-8">
<title>Corvelle Strategies – Business Card</title>
<link rel="stylesheet" href="https://fonts.googleapis.com/css2?family=Playfair+Display:wght@800&family=Poppins:wght@400;500&display=swap">
<style>
  :root {
    --stage: #1d1d20;
    --paper: #ffffff;
    --brand-blue: #0756a3;
    --accent-orange: #f4ac38;
    --text-light: #ffffff;
    --serif: "Playfair Display", Georgia, serif;
    --sans: "Poppins", Arial, sans-serif;
  }
  * { box-sizing: border-box; margin: 0; padding: 0; }
  html, body {
    width: 1200px; height: 1200px; overflow: hidden;
    background: var(--stage);
  }
  .sheet {
    width: 1200px; height: 1200px;
    display: flex; flex-direction: column; align-items: center; justify-content: center;
    gap: 50px;
  }
  .card {
    position: relative;
    width: 910px; height: 520px;
    background: var(--paper);
    overflow: hidden;
  }

  /* Front */
  .card-front {
    display: flex; align-items: center; justify-content: center;
  }
  .wordmark {
    display: flex; align-items: center; gap: 18px;
  }
  .wordmark-name {
    font-family: var(--serif);
    font-weight: 800;
    color: var(--brand-blue);
    font-size: 64px;
    letter-spacing: -1px;
    white-space: nowrap;
  }
  .wordmark-dot {
    width: 40px; height: 40px; border-radius: 50%;
    background: var(--accent-orange);
    flex: none;
  }

  /* Back */
  .brand-strip {
    position: absolute; left: 0; top: 0; bottom: 0; width: 230px;
    display: flex; align-items: center; justify-content: center;
  }
  .brand-strip .wordmark {
    transform: rotate(-90deg);
  }
  .brand-strip .wordmark-name { font-size: 40px; letter-spacing: -0.5px; }
  .brand-strip .wordmark-dot { width: 26px; height: 26px; gap: 12px; }

  .info-panel {
    position: absolute; top: 0; right: 0; bottom: 0; left: 170px;
    background: var(--brand-blue);
    clip-path: polygon(115px 0, 100% 0, 100% 100%, 0 100%);
    color: var(--text-light);
  }
  .contact-block {
    position: absolute; left: 190px; top: 205px;
  }
  .person-name {
    font-family: var(--serif);
    font-weight: 800;
    font-size: 42px;
    line-height: 1.1;
  }
  .person-title {
    font-family: var(--sans);
    font-weight: 400;
    font-size: 24px;
    margin-top: 4px;
  }
  .contact-list {
    list-style: none;
    margin-top: 34px;
    font-family: var(--sans);
    font-size: 23px;
    font-weight: 400;
  }
  .contact-list li {
    display: flex; align-items: center; gap: 18px;
    margin-bottom: 10px;
  }
  .contact-icon { width: 28px; height: 24px; flex: none; fill: var(--accent-orange); }
</style>
</head>
<body>
  <main class="sheet">
    <section class="card card-front" aria-label="Card front">
      <div class="wordmark">
        <span class="wordmark-name">Corvelle Strategies</span>
        <span class="wordmark-dot"></span>
      </div>
    </section>

    <section class="card card-back" aria-label="Card back">
      <div class="brand-strip">
        <div class="wordmark">
          <span class="wordmark-name">Corvelle Strategies</span>
          <span class="wordmark-dot"></span>
        </div>
      </div>
      <div class="info-panel">
        <div class="contact-block">
          <h1 class="person-name">Glen Mosswater</h1>
          <p class="person-title">Business Manager</p>
          <ul class="contact-list">
            <li>
              <svg class="contact-icon" viewBox="0 0 28 24" aria-hidden="true">
                <path d="M2 8c0-3 5-6 12-6s12 3 12 6v2h-6V7c-2-1-10-1-12 0v3H2z"/>
                <path d="M7 11h14l3 11H4z"/>
              </svg>
              <span>202-555-0148</span>
            </li>
            <li>
              <svg class="contact-icon" viewBox="0 0 28 24" aria-hidden="true">
                <path d="M2 4h24v16H2z M4 6l10 8 10-8" stroke="#0756a3" stroke-width="1.5"/>
              </svg>
              <span>glen@corvellestrategies-example.com</span>
            </li>
          </ul>
        </div>
      </div>
    </section>
  </main>
</body>
</html>
```